Why Use Me?

Need to create several flyers to promote myself and various home mortgage loan products. I am a loan officer within a larger company so I'm looking for an attractive flyer frame that incorporates my company's colors & logo BUT it has my own custom look and feel. Once this frame is created, I'll have several ideas for body filler. I'm looking for a logo or moniker for myself, synonymous with my business.

```html
<!DOCTYPE html>
<html lang="en">
<head>
<meta charset="utf-8">
<title>Why Use Me – Loan Officer Flyer</title>
<link href="https://fonts.googleapis.com/css2?family=Poppins:wght@400;500;600;700&family=Kaushan+Script&family=Barlow+Condensed:wght@400;500&family=Oswald:wght@600&display=swap" rel="stylesheet">
<style>
  :root{
    --mat:#a3a3a3;
    --paper:#ffffff;
    --navy:#12194a;
    --sky:#0b9be0;
    --sky-deep:#0677c4;
    --ink:#1b2356;
  }
  *{margin:0;padding:0;box-sizing:border-box}
  html,body{width:1200px;height:1200px;overflow:hidden;background:var(--mat)}
  .flyer{position:absolute;left:204px;top:87px;width:794px;height:1028px;background:var(--paper);overflow:hidden;font-family:"Poppins",sans-serif}
  .flyer-shapes{position:absolute;left:0;top:0;width:794px;height:1028px}
  .brand{position:absolute;left:66px;top:62px;display:flex;align-items:center;gap:10px}
  .brand-dot{width:16px;height:16px;border-radius:50%;background:var(--sky);flex:none}
  .brand-name{font-weight:600;font-size:22px;line-height:26px;color:var(--navy);letter-spacing:.5px}
  .tagline{position:absolute;left:66px;top:188px;font-family:"Kaushan Script",cursive;color:var(--sky);font-size:52px;line-height:80px}
  .offer-title{position:absolute;left:67px;top:390px;color:#fff;font-size:33px;font-weight:400}
  .offer-text{position:absolute;left:63px;top:443px;color:#fff;font-size:24px;line-height:42px;font-weight:400}
  .why-heading{position:absolute;left:71px;top:635px;color:var(--sky);font-weight:700;line-height:1}
  .why-heading .big{display:block;font-size:40px}
  .why-heading .small{display:block;font-size:28px;margin-top:4px}
  .why-list{position:absolute;left:71px;top:729px;list-style:none}
  .why-list li{display:flex;align-items:center;gap:14px;height:27.2px;font-size:16px;font-weight:600;color:var(--ink)}
  .why-list svg{width:13px;height:11px;flex:none}
  .agent-card{position:absolute;left:543px;top:494px;width:208px;height:391px}
  .agent-role{position:absolute;left:23px;top:221px;font-family:"Barlow Condensed",sans-serif;font-size:26px;color:#fff;font-weight:400}
  .agent-meta{position:absolute;left:24px;top:254px;font-family:"Barlow Condensed",sans-serif;font-size:12.5px;line-height:18px;color:#fff}
  .agent-phones{position:absolute;left:18px;top:313px;font-family:"Oswald",sans-serif;font-weight:600;font-size:17px;line-height:27px;color:#fff}
  .quote{position:absolute;left:171px;top:950px;width:450px;color:#fff;font-size:17px;line-height:26px;font-weight:500}
  .quote-mark{font-weight:700;font-size:22px;line-height:1;vertical-align:-4px}
  .quote-open{position:absolute;left:150px;top:953px;color:#fff}
</style>
</head>
<body>
<div class="flyer">
  <svg class="flyer-shapes" viewBox="0 0 1278 1655" preserveAspectRatio="none">
    <defs>
      <linearGradient id="officeTone" x1="0" y1="0" x2="1" y2="0">
        <stop offset="0" stop-color="#ffffff"/>
        <stop offset=".45" stop-color="#e9e2d9"/>
        <stop offset="1" stop-color="#8a7158"/>
      </linearGradient>
      <linearGradient id="officeFade" x1="0" y1="0" x2="0" y2="1">
        <stop offset="0" stop-color="#ffffff" stop-opacity=".7"/>
        <stop offset=".4" stop-color="#ffffff" stop-opacity="0"/>
      </linearGradient>
      <linearGradient id="familyTone" x1="0" y1="0" x2="1" y2="1">
        <stop offset="0" stop-color="#ece9e4"/>
        <stop offset=".5" stop-color="#b7a292"/>
        <stop offset="1" stop-color="#6f8fb4"/>
      </linearGradient>
      <linearGradient id="bandTone" x1="0" y1="0" x2="1" y2="0">
        <stop offset="0" stop-color="#0a9fe6"/>
        <stop offset=".5" stop-color="#0a62b4"/>
        <stop offset="1" stop-color="#0a9fe6"/>
      </linearGradient>
      <linearGradient id="cardTone" x1="0" y1="0" x2="0" y2="1">
        <stop offset="0" stop-color="#12194a"/>
        <stop offset=".35" stop-color="#12194a"/>
        <stop offset="1" stop-color="#0b9be0"/>
      </linearGradient>
      <linearGradient id="portraitTone" x1="0" y1="0" x2="0" y2="1">
        <stop offset="0" stop-color="#f2f3f6"/>
        <stop offset=".6" stop-color="#e6e9ef"/>
        <stop offset="1" stop-color="#3a4566"/>
      </linearGradient>
      <clipPath id="familyClip"><circle cx="1110" cy="480" r="520"/></clipPath>
    </defs>

    <rect x="0" y="950" width="1278" height="580" fill="url(#officeTone)" role="img" aria-label="Photo of a busy office desk with laptops and paperwork"/>
    <rect x="0" y="950" width="1278" height="580" fill="url(#officeFade)"/>

    <path d="M0 282 C220 240 420 230 640 234 L900 300 L1278 900 L1278 1000 C1100 1030 950 1040 820 1030 C520 1010 250 960 0 878 Z" fill="var(--navy)"/>
    <path d="M0 282 C200 245 380 234 560 234 C380 240 180 265 0 305 Z" fill="var(--sky)"/>
    <path d="M0 878 C250 960 520 1010 820 1030 C950 1040 1100 1030 1278 1000 L1278 1030 C1100 1050 950 1055 820 1048 C520 1030 250 980 0 878 Z" fill="var(--sky)"/>

    <circle cx="1080" cy="480" r="565" fill="var(--sky)"/>
    <g clip-path="url(#familyClip)">
      <rect x="560" y="-60" width="800" height="1080" fill="url(#familyTone)" role="img" aria-label="Photo of a smiling family unpacking a moving box on the sofa"/>
    </g>

    <path d="M152 1520 L1090 1520 L1002 1655 L252 1655 Z" fill="var(--navy)"/>
    <path d="M0 1550 L130 1550 L252 1655 L0 1655 Z" fill="url(#bandTone)"/>
    <path d="M1110 1550 L1278 1550 L1278 1655 L1002 1655 Z" fill="url(#bandTone)"/>

    <path d="M876 830 L1208 830 L1208 1380 Q1208 1422 1166 1422 L918 1422 Q876 1422 876 1380 Z" fill="url(#cardTone)"/>
    <circle cx="1041" cy="970" r="170" fill="var(--sky)"/>
    <circle cx="1041" cy="970" r="160" fill="url(#portraitTone)" role="img" aria-label="Portrait photo of the loan officer in a dark suit"/>
  </svg>

  <div class="brand"><span class="brand-dot"></span><span class="brand-name">SUMMIT CREST<br>LENDING</span></div>

  <div class="tagline">Life takes<br>you places</div>
  <h2 class="offer-title">We Offer</h2>
  <p class="offer-text">Summit Crest Lending<br>takes you Home</p>

  <h1 class="why-heading"><span class="big">Concerning</span><span class="small">why use me:</span></h1>
  <ul class="why-list">
    <li><svg viewBox="0 0 13 11"><path d="M1 6 L5 10 L12 1" stroke="var(--ink)" stroke-width="2.6" fill="none"/></svg>I’m 17 years at the same exact mortgage company</li>
    <li><svg viewBox="0 0 13 11"><path d="M1 6 L5 10 L12 1" stroke="var(--ink)" stroke-width="2.6" fill="none"/></svg>Very knowledgeable</li>
    <li><svg viewBox="0 0 13 11"><path d="M1 6 L5 10 L12 1" stroke="var(--ink)" stroke-width="2.6" fill="none"/></svg>Above and beyond service and availability</li>
    <li><svg viewBox="0 0 13 11"><path d="M1 6 L5 10 L12 1" stroke="var(--ink)" stroke-width="2.6" fill="none"/></svg>Conversion of tough loans</li>
    <li><svg viewBox="0 0 13 11"><path d="M1 6 L5 10 L12 1" stroke="var(--ink)" stroke-width="2.6" fill="none"/></svg>“Build a Buyer” program</li>
    <li><svg viewBox="0 0 13 11"><path d="M1 6 L5 10 L12 1" stroke="var(--ink)" stroke-width="2.6" fill="none"/></svg>Excellent follow-up</li>
    <li><svg viewBox="0 0 13 11"><path d="M1 6 L5 10 L12 1" stroke="var(--ink)" stroke-width="2.6" fill="none"/></svg>I work with a seasoned lending team</li>
  </ul>

  <div class="agent-card">
    <div class="agent-role">Sr. Loan Officer</div>
    <div class="agent-meta">NMLS# 482019<br>Licensed States: NV, TX, AZ, OR<br>FHA, Conventional, VA, Private Money</div>
    <div class="agent-phones">Office: (555) 014-2290<br>Cell: (555) 017-4481</div>
  </div>

  <span class="quote-mark quote-open">“</span>
  <p class="quote">Mortgage marketing material must contain certain legal verbiage that I’ll need to eventually provide <span class="quote-mark">”</span></p>
</div>
</body>
</html>
```